NEW Escape Room. Fun, Dark and Mysterious.

Escape Room Website. Bookings and scheduling of appointments will be organised with Bookvane through the site. Most appointments will be created online through the booking system with some payments coming through in person by drop-ins. Groups will be from 2 - 8 people with a sliding scale of prices. We will start with one game playable and one saying coming soon. We will also eventually have 4 games up and running at once so will need it to be able to expand. We don't have any images of the rooms because it all relies heavily on mystery. Appointments are each 1 hour long with 30 minutes in between.

Target Market(s)

15-35 year olds

Coding

Coded - Design and coding required

Number of Pages Required

5+ page

Font styles to use
Decorative

Colors

Designer to choose colors to be used in the design.

Requirements
Must have
• Graphics showing what an escape room is.
• Page for About - What is an escape room
• Page for Games - Showing each of the different games which can be played with links to booking page. We have one game to start - the surgeons shadows. A victorian doctors office and serial killers. Then a game coming soon which is aztec/mayan/jungle/harold Crane feel.
• FAQ Page
Nice to have
• Graphics for multiple players ie 2 players, 3 players, 4 players etc
• Dark and Mysterious feel.
• Inspiration from Puzzle Vault, Cipher Lodge, Quest Lockbox
Should not have
• Cartoony/childish. Pink.
• Not bloody or dripping letters etc - not cliche.
• Not horror themed.

```html
<!DOCTYPE html>
<html lang="en">
<head>
<meta charset="UTF-8">
<title>The Hidden Door — Escape Room</title>
<link rel="stylesheet" href="https://fonts.googleapis.com/css2?family=Teko:wght@400;500;600&family=Montserrat:wght@400&display=swap">
<style>
  :root {
    --ink: #04060a;
    --gold: #fdb827;
    --white: #ffffff;
    --rule: rgba(255, 255, 255, 0.28);
    --teal-deep: #0d2a33;
    --teal-mid: #1b4452;
    --dusk: #3a2a38;
  }
  * { margin: 0; padding: 0; box-sizing: border-box; }
  html, body {
    width: 1200px;
    height: 750px;
    overflow: hidden;
    background: var(--ink);
  }
  .hero {
    position: relative;
    width: 1200px;
    height: 750px;
    overflow: hidden;
    background: var(--ink);
  }
  .hero-backdrop {
    position: absolute;
    inset: 0;
    background:
      radial-gradient(ellipse 70px 60px at 620px 390px, rgba(160, 120, 150, 0.55), transparent 100%),
      radial-gradient(ellipse 260px 300px at 610px 420px, rgba(27, 68, 82, 0.75), transparent 100%),
      radial-gradient(ellipse 420px 380px at 610px 430px, rgba(13, 42, 51, 0.8), transparent 100%),
      radial-gradient(ellipse 700px 500px at 600px 420px, rgba(10, 22, 28, 0.9), transparent 100%),
      var(--ink);
  }
  .site-nav {
    position: absolute;
    left: 300px;
    top: 66px;
    width: 600px;
    height: 46px;
    border-top: 1px solid var(--rule);
    border-bottom: 1px solid var(--rule);
  }
  .nav-link {
    position: absolute;
    top: 4px;
    font-family: "Teko", sans-serif;
    font-weight: 500;
    font-size: 32px;
    line-height: 40px;
    color: var(--gold);
    text-decoration: none;
    letter-spacing: 0.3px;
  }
  .nav-about { left: 0; }
  .nav-games { left: 133px; }
  .nav-faq { left: 397px; }
  .nav-contact { right: 0; }
  .brand {
    position: absolute;
    left: 540px;
    top: 52px;
    width: 120px;
    height: 74px;
    display: flex;
    flex-direction: column;
    align-items: center;
    justify-content: center;
    gap: 4px;
  }
  .brand-square {
    width: 14px;
    height: 14px;
    background: var(--gold);
  }
  .brand-name {
    font-family: "Teko", sans-serif;
    font-weight: 500;
    font-size: 22px;
    line-height: 22px;
    color: var(--gold);
    white-space: nowrap;
  }
  .hero-tagline {
    position: absolute;
    left: 84px;
    top: 242px;
    font-family: "Teko", sans-serif;
    font-weight: 500;
    font-size: 29px;
    line-height: 34px;
    color: var(--white);
  }
  .hero-tagline .accent { color: var(--gold); }
  .hero-title {
    position: absolute;
    left: 82px;
    top: 292px;
    font-family: "Teko", sans-serif;
    font-weight: 600;
    font-size: 158px;
    line-height: 140px;
    color: var(--gold);
    white-space: nowrap;
    letter-spacing: 1px;
  }
  .book-button {
    position: absolute;
    left: 83px;
    top: 450px;
    width: 159px;
    height: 56px;
    border: 1px solid var(--gold);
    padding: 3px;
    text-decoration: none;
  }
  .book-button-inner {
    width: 100%;
    height: 100%;
    border: 1px solid var(--gold);
    display: flex;
    align-items: center;
    justify-content: center;
    font-family: "Teko", sans-serif;
    font-weight: 500;
    font-size: 24px;
    padding-top: 4px;
    color: var(--gold);
  }
  .audience-note {
    position: absolute;
    left: 257px;
    top: 472px;
    font-family: "Montserrat", sans-serif;
    font-size: 10px;
    line-height: 14px;
    color: #e9d9a8;
  }
</style>
</head>
<body>
  <main class="hero">
    <div class="hero-backdrop" role="img" aria-label="Photograph of a dark, crumbling concrete corridor with rubble on the floor, lit in cold teal with faint pink light at the far end"></div>

    <nav class="site-nav">
      <a class="nav-link nav-about" href="#about">ABOUT</a>
      <a class="nav-link nav-games" href="#games">GAMES</a>
      <a class="nav-link nav-faq" href="#faq">FAQ</a>
      <a class="nav-link nav-contact" href="#contact">CONTACT US</a>
    </nav>

    <a class="brand" href="#home" aria-label="The Hidden Door home">
      <span class="brand-square"></span>
      <span class="brand-name">The Hidden Door</span>
    </a>

    <p class="hero-tagline">Most Immersive <span class="accent">Escape Room</span> Experience</p>
    <h1 class="hero-title">The Hidden Door</h1>

    <a class="book-button" href="#book"><span class="book-button-inner">Book Now</span></a>
    <p class="audience-note">Suitable For Family/Corporate/Friends</p>
  </main>
</body>
</html>
```